Business card design needed with logo

My business is called KVM Solutions & it is targeted towards mobile equipment maintenance in the Mining and civil industry. My work involves maintenance planning and maintenance management plus also supply tradespeople on a labour hire basis. We can provide from basic shut-down machine rebuild plans to complete rebuild services supply plans and labour to anywhere in Australia. I would like to use the colours Black, Red and Grey, I had done a desgin as attached but doesn't really explain what we do and gears don't embroider well onto shirts.
Updates

I also wanted to see the something replace the gears maybe just making the KVM lettering look a bit different or put together differently 

Hello I have extended the deadline by a few extra days as I would like to update details on the front of card, details below & can be put which ever way looks good;

Liam Fenwick
Director
0417263958
KVM@mailnest.com.au
www.kvmsolutions-demo.com.au

On the back of the card I would like to have the below printed;

Capable of providing, but not limited to, across Australia:
- Contract Maintenance Planning.
- Skilled Mobile Maintenance labour hire.
- New machine build specifications. 
- Plant risk assessments and inspections.
- Shut down and rebuild program planning.
- Preventative maintenance tasks, including build of materials lists, creation and review.

Target Market(s)

Contractors and companies that use small and large earthmoving and mining machines

Industry/Entity Type

Business

Contact Information for Business Card

Trading name is KVM Solutions
My name and title is
Liam Fenwick Director
0417 263 958
KVM@mailnest.com.au

Logo Text

KVM

```html
<!DOCTYPE html>
<html lang="en">
<head>
<meta charset="UTF-8">
<title>KVM Solutions Business Card</title>
<link href="https://fonts.googleapis.com/css2?family=Roboto+Condensed:wght@400;700&family=Roboto:wght@400;500&display=swap" rel="stylesheet">
<style>
  :root {
    --backdrop: #3b4756;
    --card-white: #f2f2f2;
    --band-grey: #8a8a8a;
    --accent-red: #c8102e;
    --ink-dark: #1f1f1f;
    --ink-mid: #555555;
    --card-charcoal: #24272c;
    --ink-light: #d9dadc;
    --silver-light: #e6e7e8;
    --silver-dark: #a9aaac;
  }
  * { margin: 0; padding: 0; box-sizing: border-box; }
  html, body {
    width: 1200px; height: 1000px; overflow: hidden;
    background: var(--backdrop);
  }
  .canvas { position: relative; width: 1200px; height: 1000px; }

  .card {
    position: absolute; left: 270px; width: 660px; height: 377px;
    box-shadow: 0 10px 24px rgba(0,0,0,0.35);
    overflow: hidden;
  }
  .card--front { top: 90px; background: var(--card-white); }
  .card--back { top: 530px; background: var(--card-charcoal); }

  /* front */
  .side-band {
    position: absolute; left: 0; top: 0; width: 56px; height: 100%;
    background: var(--band-grey);
  }
  .side-band__accent {
    position: absolute; left: 0; top: 228px; width: 76px; height: 28px;
    background: var(--accent-red);
    border-top: 4px solid var(--card-white);
    border-bottom: 4px solid var(--card-white);
    box-sizing: content-box;
  }
  .corner-square {
    position: absolute; right: 0; top: 32px; width: 34px; height: 34px;
    background: var(--band-grey);
  }
  .holder {
    position: absolute; right: 48px; top: 30px; text-align: right;
    font-family: "Roboto Condensed", sans-serif;
  }
  .holder__name {
    color: var(--accent-red); font-weight: 700; font-size: 26px;
    letter-spacing: 0.5px; line-height: 1;
  }
  .holder__title {
    color: var(--ink-mid); font-size: 12px; font-weight: 400; margin-top: 1px;
  }
  .accent-bar {
    position: absolute; right: 0; top: 150px; width: 375px; height: 24px;
    background: var(--accent-red);
  }
  .company {
    position: absolute; left: 96px; top: 168px;
    font-family: "Roboto Condensed", sans-serif; font-weight: 700;
    font-size: 42px; color: var(--ink-dark); letter-spacing: 0.3px;
  }
  .contact {
    position: absolute; left: 100px; top: 236px; list-style: none;
    font-family: "Roboto", sans-serif; font-size: 14px; color: var(--ink-mid);
  }
  .contact__item { display: flex; align-items: center; gap: 10px; margin-bottom: 8px; }
  .contact__icon { width: 14px; height: 14px; flex: none; }

  /* back */
  .silver-band {
    position: absolute; left: 0; top: 26px; width: 100%; height: 96px;
    background: linear-gradient(90deg, var(--silver-dark) 0%, var(--silver-light) 45%, var(--silver-light) 60%, var(--silver-dark) 100%);
    display: flex; align-items: center; justify-content: center; gap: 12px;
  }
  .brand-name {
    font-family: "Roboto Condensed", sans-serif; font-weight: 700;
    font-size: 56px; color: var(--card-charcoal); letter-spacing: 1px;
  }
  .brand-dot {
    width: 22px; height: 22px; border-radius: 50%; background: var(--accent-red);
  }
  .services {
    position: absolute; left: 44px; right: 40px; top: 146px;
    font-family: "Roboto", sans-serif; color: var(--ink-light);
  }
  .services__heading {
    font-family: "Roboto Condensed", sans-serif; font-weight: 700;
    font-size: 15px; color: #ffffff; margin-bottom: 10px;
  }
  .services__list { list-style: none; font-size: 12.5px; line-height: 1.6; }
  .services__item { position: relative; padding-left: 16px; }
  .services__item::before {
    content: ""; position: absolute; left: 0; top: 7px;
    width: 7px; height: 7px; background: var(--accent-red);
  }
</style>
</head>
<body>
<main class="canvas">
  <section class="card card--front">
    <div class="side-band"></div>
    <div class="side-band__accent"></div>
    <div class="corner-square"></div>
    <div class="holder">
      <p class="holder__name">LIAM FENWICK</p>
      <p class="holder__title">Director</p>
    </div>
    <div class="accent-bar"></div>
    <h1 class="company">KVM SOLUTIONS</h1>
    <ul class="contact">
      <li class="contact__item">
        <svg class="contact__icon" viewBox="0 0 16 16"><circle cx="8" cy="8" r="7" fill="none" stroke="#c8102e" stroke-width="1.6"/><path d="M5.5 4.5l1.5 0 0.8 2-1 0.8a5 5 0 0 0 2 2l0.8-1 2 0.8 0 1.5c-3.5 0.5-6.6-2.6-6.1-6.1z" fill="#c8102e"/></svg>
        <span>0417 263 958</span>
      </li>
      <li class="contact__item">
        <svg class="contact__icon" viewBox="0 0 16 16"><rect x="1" y="3" width="14" height="10" rx="1" fill="#c8102e"/><path d="M1.5 3.5l6.5 5 6.5-5" fill="none" stroke="#f2f2f2" stroke-width="1.3"/></svg>
        <span>KVM@mailnest.com.au</span>
      </li>
      <li class="contact__item">
        <svg class="contact__icon" viewBox="0 0 16 16"><circle cx="8" cy="8" r="7" fill="none" stroke="#c8102e" stroke-width="1.4"/><ellipse cx="8" cy="8" rx="3" ry="7" fill="none" stroke="#c8102e" stroke-width="1.2"/><path d="M1 8h14" stroke="#c8102e" stroke-width="1.2"/></svg>
        <span>www.kvmsolutions-demo.com.au</span>
      </li>
    </ul>
  </section>

  <section class="card card--back">
    <div class="silver-band">
      <span class="brand-name">KVM</span>
      <span class="brand-dot"></span>
    </div>
    <div class="services">
      <p class="services__heading">Capable of providing, but not limited to, across Australia:</p>
      <ul class="services__list">
        <li class="services__item">Contract Maintenance Planning.</li>
        <li class="services__item">Skilled Mobile Maintenance labour hire.</li>
        <li class="services__item">New machine build specifications.</li>
        <li class="services__item">Plant risk assessments and inspections.</li>
        <li class="services__item">Shut down and rebuild program planning.</li>
        <li class="services__item">Preventative maintenance tasks, including build of materials lists, creation and review.</li>
      </ul>
    </div>
  </section>
</main>
</body>
</html>
```